Multiple website banners for a shopify theme

I need custom designed banners for a destributor webpage.

We will be selling products in our local store from a supplier https://pipwellsoaps.co.uk (you can get the ideas from their site).

We need custom desings:
- 2-3x 1920x745
- 1x 960x960
- 2x 480x480
- 1x 960*480
All of theme need to nicely fit together as shown in the uploaded layout screenshot (website_banner_layout).
In Google drive link there are products pictures which must be used in the banners.

https://files.mornavex.com/share/folders/8QpTzK2wLmVa7HnYcRbE5dUsXoGi3JfKt?usp=sharing

Target Market(s)

Kids, Cosmetics market

Industry/Entity Type

Cosmetics

Requirements
Must have
• Playful elements

```html
<!DOCTYPE html>
<html lang="en">
<head>
<meta charset="utf-8">
<title>Pipwell Kozmetika – Website Banner Set</title>
<link rel="stylesheet" href="https://fonts.googleapis.com/css2?family=Fredoka:wght@500;600;700&family=Sniglet&family=Luckiest+Guy&family=Poppins&display=swap">
<style>
:root{
  --page:#dcdcdc;
  --pink-base:#f9a5cc;
  --pink-soft:#fbbcdb;
  --pink-hot:#f84f9c;
  --pink-deep:#c6076a;
  --pink-text:#e3157d;
  --white:#ffffff;
  --cyan:#16c1e8;
  --tan:#c38a80;
  --navy:#232f6a;
  --label:#1e1e1e;
}
*{margin:0;padding:0;box-sizing:border-box}
html,body{width:835px;height:1200px;overflow:hidden;background:var(--page)}
.board{position:relative;width:835px;height:1200px}
.banner{position:absolute;overflow:hidden;background:var(--pink-base);box-shadow:6px 8px 10px rgba(0,0,0,.28)}
.banner-bg{position:absolute;inset:0;width:100%;height:100%}
.size-label{position:absolute;font-family:"Poppins",sans-serif;font-size:20px;color:var(--label);transform:translateX(-50%);white-space:nowrap}
.brand{position:absolute;display:flex;align-items:center;gap:5px;z-index:2}
.brand-dot{border-radius:50%;background:var(--pink-hot);flex:none}
.brand-name{font-family:"Fredoka",sans-serif;font-weight:700;color:var(--white);line-height:1;white-space:nowrap}
.headline{position:absolute;font-family:"Fredoka",sans-serif;font-weight:700;color:var(--white);line-height:.95;letter-spacing:-.5px;z-index:2}
.tagline{position:absolute;font-family:"Sniglet",sans-serif;color:var(--pink-text);line-height:1.05;z-index:2}
.shop-btn{position:absolute;display:flex;align-items:center;justify-content:center;background:var(--pink-deep);border-radius:999px;font-family:"Luckiest Guy",sans-serif;font-weight:700;text-transform:uppercase;color:var(--white);letter-spacing:.5px;padding-top:2px;z-index:2;white-space:nowrap}
.sticker{position:absolute;border-radius:50%;display:flex;flex-direction:column;align-items:center;justify-content:center;font-family:"Fredoka",sans-serif;font-weight:700;color:var(--white);transform:rotate(12deg);line-height:.9;z-index:3}
.sticker small{display:block;font-size:.36em;font-weight:600;align-self:flex-end;margin-right:22%}
.sticker--cyan{background:var(--cyan)}
.sticker--tan{background:var(--tan)}
.sticker--navy{background:var(--navy)}
.product{position:absolute;border-radius:46% 54% 40% 60% / 55% 45% 55% 45%;z-index:1}
</style>
</head>
<body>
<main class="board">

  <!-- Hero 1920 x 745 -->
  <section class="banner banner--hero" style="left:70px;top:85px;width:694px;height:269px">
    <svg class="banner-bg" viewBox="0 0 694 269" preserveAspectRatio="none" aria-hidden="true">
      <path d="M0 190 C60 170 120 215 200 240 C260 258 300 269 320 269 L0 269Z" fill="var(--pink-soft)"/>
      <path d="M120 0 C180 20 260 10 340 0Z" fill="var(--pink-soft)"/>
      <path d="M340 0 L694 0 L694 269 L570 269 C560 240 520 235 470 240 C420 245 380 225 400 195 C420 165 390 150 410 120 C430 90 370 60 372 30 C374 10 350 5 340 0Z" fill="var(--pink-hot)"/>
      <path d="M600 40 C640 20 680 30 694 35 L694 110 C660 100 630 80 600 40Z" fill="var(--pink-base)" opacity=".55"/>
      <circle cx="349" cy="219" r="20" fill="var(--pink-hot)"/><circle cx="360" cy="219" r="6" fill="var(--pink-soft)"/>
      <circle cx="383" cy="233" r="8" fill="var(--pink-hot)"/>
      <circle cx="8" cy="255" r="10" fill="var(--pink-hot)"/>
    </svg>
    <div class="brand" style="left:32px;top:52px">
      <span class="brand-dot" style="width:22px;height:22px"></span>
      <span class="brand-name" style="font-size:26px">Pipwell Kozmetika</span>
    </div>
    <h1 class="headline" style="left:32px;top:120px;font-size:41px">Fizz Blasters</h1>
    <p class="tagline" style="left:32px;top:162px;font-size:24px">You know it makes scents</p>
    <a class="shop-btn" style="left:34px;top:203px;width:124px;height:32px;font-size:16px">Shop Now</a>
    <div class="sticker sticker--cyan" style="left:301px;top:21px;width:92px;height:92px;font-size:32px">30%<small>OFF</small></div>
    <div class="product" role="img" aria-label="Photo of three colourful bath bombs: a rainbow-topped ball, a purple heart and a yellow-pink ball with a strawberry"
      style="left:415px;top:8px;width:250px;height:226px;background:radial-gradient(circle at 30% 70%,#7fc6ec,transparent 40%),radial-gradient(circle at 72% 72%,#f6d228,transparent 45%),radial-gradient(circle at 50% 25%,#8a3fc2,transparent 40%),#f06fb0"></div>
  </section>
  <p class="size-label" style="left:426px;top:372px">1920 X 745</p>

  <!-- Square 960 x 960 -->
  <section class="banner banner--square" style="left:111px;top:433px;width:366px;height:366px">
    <svg class="banner-bg" viewBox="0 0 366 366" preserveAspectRatio="none" aria-hidden="true">
      <path d="M0 280 C50 260 110 290 150 320 C180 345 150 366 150 366 L0 366Z" fill="var(--pink-soft)"/>
      <path d="M160 240 C230 215 300 225 366 220 L366 366 L110 366 C140 340 200 330 230 300 C250 280 150 270 160 240Z" fill="var(--pink-hot)"/>
      <path d="M220 310 C260 290 320 300 366 290 L366 340 C330 345 270 345 220 310Z" fill="var(--pink-base)" opacity=".7"/>
      <path d="M100 0 L366 0 L366 60 C320 50 260 20 100 0Z" fill="var(--pink-soft)" opacity=".6"/>
      <circle cx="176" cy="10" r="22" fill="var(--pink-hot)"/><circle cx="179" cy="9" r="6" fill="var(--pink-soft)"/>
      <circle cx="196" cy="36" r="9" fill="var(--pink-hot)"/>
      <circle cx="14" cy="238" r="13" fill="var(--pink-hot)"/><circle cx="13" cy="238" r="4" fill="var(--pink-soft)"/>
    </svg>
    <div class="brand" style="left:232px;top:38px;gap:6px">
      <span class="brand-dot" style="width:18px;height:18px"></span>
      <span class="brand-name" style="font-size:20px">Pipwell<br>Kozmetika</span>
    </div>
    <h2 class="headline" style="left:28px;top:30px;font-size:39px">Sugar<br>Berry<br>Sprite</h2>
    <p class="tagline" style="left:29px;top:151px;font-size:24px">Gift Pack</p>
    <div class="product" role="img" aria-label="Photo of a lip-print wrapped gift box with a red ribbon, bath bombs, a soap and a bath cupcake"
      style="left:150px;top:112px;width:210px;height:185px;background:radial-gradient(circle at 45% 30%,#e43c8c,transparent 45%),radial-gradient(circle at 60% 80%,#f1dce2,transparent 45%),#f37fb5"></div>
    <div class="sticker sticker--tan" style="left:69px;top:206px;width:70px;height:70px;font-size:25px">30%<small>OFF</small></div>
    <a class="shop-btn" style="left:29px;top:306px;width:103px;height:27px;font-size:14px">Shop Now</a>
  </section>
  <p class="size-label" style="left:293px;top:811px">960 X 960</p>

  <!-- Small square 480 x 480 -->
  <section class="banner banner--small" style="left:547px;top:517px;width:201px;height:200px">
    <svg class="banner-bg" viewBox="0 0 201 200" preserveAspectRatio="none" aria-hidden="true">
      <path d="M50 145 C100 130 150 140 201 135 L201 200 L80 200 C95 185 120 175 80 168 C60 165 40 155 50 145Z" fill="var(--pink-hot)"/>
      <path d="M0 160 C40 150 70 170 80 200 L0 200Z" fill="var(--pink-soft)"/>
      <path d="M0 0 L201 0 L201 25 C150 20 110 8 0 0Z" fill="var(--pink-soft)" opacity=".6"/>
      <circle cx="91" cy="6" r="11" fill="var(--pink-hot)"/><circle cx="105" cy="21" r="5" fill="var(--pink-hot)"/>
      <circle cx="6" cy="133" r="6" fill="var(--pink-hot)"/>
    </svg>
    <div class="brand" style="left:124px;top:22px;gap:3px">
      <span class="brand-dot" style="width:10px;height:10px"></span>
      <span class="brand-name" style="font-size:11px">Pipwell<br>Kozmetika</span>
    </div>
    <h2 class="headline" style="left:13px;top:18px;font-size:21px">Glow<br>Candles</h2>
    <p class="tagline" style="left:13px;top:65px;font-size:12px">Enhances<br>your mood</p>
    <div class="product" role="img" aria-label="Photo of scented candles in glass jars with their patterned gift boxes"
      style="left:80px;top:63px;width:115px;height:104px;background:radial-gradient(circle at 25% 40%,#8ab6ea,transparent 45%),radial-gradient(circle at 80% 30%,#6e9a5c,transparent 35%),#e7e2ef"></div>
    <div class="sticker sticker--cyan" style="left:35px;top:105px;width:38px;height:38px;font-size:13px">30%<small>OFF</small></div>
    <a class="shop-btn" style="left:13px;top:166px;width:65px;height:13px;font-size:7px;padding-top:1px">Shop Now</a>
  </section>
  <p class="size-label" style="left:646px;top:731px">480 X 480</p>

  <!-- Wide 960 x 480 -->
  <section class="banner banner--wide" style="left:220px;top:881px;width:411px;height:205px">
    <svg class="banner-bg" viewBox="0 0 411 205" preserveAspectRatio="none" aria-hidden="true">
      <path d="M0 150 C40 140 90 160 120 180 C140 195 130 205 130 205 L0 205Z" fill="var(--pink-soft)"/>
      <path d="M150 50 C200 30 240 40 280 20 C320 5 360 0 411 0 L411 205 L240 205 C225 185 230 170 245 160 C265 145 230 130 240 110 C250 90 210 80 190 70 C170 62 150 60 150 50Z" fill="var(--pink-hot)"/>
      <path d="M0 0 L200 0 C160 12 90 8 0 20Z" fill="var(--pink-soft)" opacity=".6"/>
      <circle cx="197" cy="182" r="13" fill="var(--pink-hot)"/><circle cx="199" cy="181" r="4" fill="var(--pink-soft)"/>
      <circle cx="214" cy="197" r="5" fill="var(--pink-hot)"/>
    </svg>
    <div class="brand" style="left:22px;top:28px">
      <span class="brand-dot" style="width:13px;height:13px"></span>
      <span class="brand-name" style="font-size:15px">Pipwell Kozmetika</span>
    </div>
    <h2 class="headline" style="left:22px;top:69px;font-size:30px">Chocolate<br>Treasure</h2>
    <p class="tagline" style="left:23px;top:131px;font-size:16px">Gift Pack</p>
    <a class="shop-btn" style="left:22px;top:163px;width:85px;height:22px;font-size:11px">Shop Now</a>
    <div class="product" role="img" aria-label="Photo of a dotted chocolate gift box with a gold ribbon surrounded by chocolate bath truffles"
      style="left:200px;top:22px;width:190px;height:160px;background:radial-gradient(circle at 40% 30%,#f4f1ee,transparent 45%),radial-gradient(circle at 60% 75%,#c79a86,transparent 45%),#ead8cf"></div>
    <div class="sticker sticker--navy" style="left:323px;top:16px;width:60px;height:60px;font-size:21px">30%<small>OFF</small></div>
  </section>
  <p class="size-label" style="left:423px;top:1105px">960 X 480</p>

</main>
</body>
</html>
```